Parent company of several different entertainment businesses needs urgent business card design

We need a business card design for key senior staff. The company name is "Bramblewick Leisure", with full legal name being Bramblewick Leisure Group Pte Ltd. No logo is required, just an update to existing design (which is a bit bland). Need to use a similar script font as the "Bramblewick" in attached. The "Entertainment" can be on a second line if required, with emphasis on the "Bramblewick". Will need to make a quick decision within 24hrs.
We operate in Asia, and Australia/NZ. Brands we work with include (www.hopvarle.example.au and www.quillmarsh-play.example and www.rendovaup.example). We will need to depict these brand logos on the back of the card. Require artwork file in eps so as can change names etc for additional staff. Thanks
Updates

Target Market(s)

Corporate target (This is the parent company, not the super fun entertainment outlets)

Industry/Entity Type

Business

Contact Information for Business Card

Name: Dorian Pellacott
Title: Executive Director
Email: dorian@bramblewick-leisure.example
Phone: +65 9000 0000
Address: 14 Fennick Rd, #05-03 Halvorne Plaza, Singapore 200000

Requirements
Should not have
• No picture logo required. Just use the company name, with emphasis on "Bramblewick"

```html
<!DOCTYPE html>
<html lang="en">
<head>
<meta charset="UTF-8">
<title>Bramblewick Leisure – Business Card</title>
<link rel="stylesheet" href="https://fonts.googleapis.com/css2?family=Lobster&family=Montserrat:wght@400;500;700&display=swap">
<style>
  :root {
    --page-bg: #e9e9ea;
    --card-black: #111111;
    --card-white: #f7f7f6;
    --navy: #1c3563;
    --ink: #2b2b2b;
    --accent-blue: #3a8fd6;
    --white: #ffffff;
  }
  * { box-sizing: border-box; margin: 0; padding: 0; }
  html, body {
    width: 1200px;
    height: 1000px;
    overflow: hidden;
    background: var(--page-bg);
    font-family: "Montserrat", Arial, sans-serif;
  }
  .sheet {
    width: 1200px;
    height: 1000px;
    display: flex;
    flex-direction: column;
    align-items: center;
    justify-content: center;
    gap: 60px;
  }
  .card {
    width: 630px;
    height: 360px;
    position: relative;
    box-shadow: 0 6px 18px rgba(0,0,0,0.18);
  }
  /* Front */
  .card--front {
    background: var(--card-black);
    display: flex;
    align-items: center;
    justify-content: center;
  }
  .wordmark {
    display: flex;
    flex-direction: column;
    align-items: flex-end;
    color: var(--white);
  }
  .wordmark__name {
    font-family: "Lobster", "Brush Script MT", cursive;
    font-weight: 400;
    font-size: 92px;
    line-height: 1;
  }
  .wordmark__legal {
    margin-top: 2px;
    padding: 2px 4px;
    border-top: 1px solid var(--white);
    border-bottom: 1px solid var(--white);
    font-weight: 400;
    font-size: 12px;
    letter-spacing: 1.6px;
    text-transform: uppercase;
  }
  /* Back */
  .card--back {
    background: var(--card-white);
  }
  .contact {
    position: absolute;
    right: 40px;
    top: 128px;
    text-align: right;
    color: var(--ink);
  }
  .contact__name {
    color: var(--navy);
    font-weight: 700;
    font-size: 20px;
    letter-spacing: 0.5px;
    text-transform: uppercase;
    line-height: 1.1;
  }
  .contact__title {
    font-weight: 700;
    font-size: 10.5px;
    margin-top: 1px;
  }
  .rule {
    position: absolute;
    left: 150px;
    right: 40px;
    top: 171px;
    height: 2px;
    background: var(--navy);
  }
  .details {
    position: absolute;
    right: 40px;
    top: 182px;
    text-align: right;
    color: var(--ink);
    font-size: 13px;
    line-height: 1.3;
  }
  .details__line {
    display: flex;
    justify-content: flex-end;
    align-items: center;
    gap: 6px;
  }
  .details__phone { margin-top: 6px; }
  .details__web {
    color: var(--navy);
    font-weight: 700;
  }
  .icon { width: 13px; height: 13px; flex: none; }
</style>
</head>
<body>
<main class="sheet">
  <section class="card card--front" aria-label="Card front">
    <div class="wordmark">
      <span class="wordmark__name">Bramblewick</span>
      <span class="wordmark__legal">Bramblewick Leisure Group Pte Ltd</span>
    </div>
  </section>

  <section class="card card--back" aria-label="Card back">
    <div class="contact">
      <p class="contact__name">Dorian Pellacott</p>
      <p class="contact__title">Executive Director</p>
    </div>
    <div class="rule"></div>
    <div class="details">
      <p>14 Fennick Rd, #05-03</p>
      <p>Halvorne Plaza,</p>
      <p>Singapore 200000</p>
      <p class="details__line details__phone">
        <svg class="icon" viewBox="0 0 14 14" aria-hidden="true">
          <circle cx="7" cy="7" r="7" fill="var(--accent-blue)"/>
          <path d="M4.6 3.6l1.3 1.6-.7.9c.5 1 1.3 1.8 2.3 2.3l.9-.7 1.6 1.3-.8 1.2C6.7 10 4 7.3 3.4 4.4z" fill="#fff"/>
        </svg>
        +65 9000 0000
      </p>
      <p class="details__line">
        <svg class="icon" viewBox="0 0 14 14" aria-hidden="true">
          <circle cx="7" cy="7" r="6.3" fill="none" stroke="var(--accent-blue)" stroke-width="1.2"/>
          <rect x="3.8" y="4.8" width="6.4" height="4.4" fill="none" stroke="var(--accent-blue)" stroke-width="1"/>
          <path d="M3.8 4.8L7 7.3l3.2-2.5" fill="none" stroke="var(--accent-blue)" stroke-width="1"/>
        </svg>
        dorian@bramblewick-leisure.example
      </p>
      <p class="details__web">www.hopvarle.example.sg</p>
    </div>
  </section>
</main>
</body>
</html>
```